Elegant, Playful, Health And Wellness Packaging Design for an Essential Oil Diffuser

Box design for diffuser, should be elegant, luxury, white box with gold foil and vibrant color combination that pops off the white box.

Designs look the same

```html
<!DOCTYPE html>
<html lang="en">
<head>
<meta charset="utf-8">
<title>Lumerra Aeri Diffuser – Box Dieline</title>
<link href="https://fonts.googleapis.com/css2?family=Oswald:wght@400;500&family=Tinos&display=swap" rel="stylesheet">
<style>
  :root {
    --stage: #465fe0;
    --navy: #15206f;
    --navy-pattern: #1f2c8c;
    --gold: #d4a62a;
    --gold-line: #e0b838;
    --paper: #ffffff;
  }
  html, body { margin: 0; padding: 0; overflow: hidden; }
  body { width: 1200px; height: 1200px; background: var(--stage); }
  .dieline { position: absolute; left: 30px; top: 238px; width: 1140px; height: 723px; }
  .paper { fill: var(--paper); }
  .navy { fill: var(--navy); }
  .pattern { fill: var(--navy-pattern); }
  .gold-band { fill: var(--gold-line); }
  .gold-dot { fill: var(--gold); }
  .heading { font-family: 'Oswald', sans-serif; font-weight: 500; }
  .tagline { fill: var(--gold); font-size: 24px; }
  .brand { fill: var(--gold); font-size: 22px; letter-spacing: 3px; }
  .brand-navy { fill: var(--navy); font-size: 19px; letter-spacing: 3px; }
  .product { fill: var(--gold); font-size: 60px; }
  .collection { fill: var(--navy); font-size: 24px; }
  .subtitle { fill: var(--navy); font-size: 19px; }
  .pill-label { fill: var(--paper); font-size: 22px; }
  .bullet { font-family: 'Oswald', sans-serif; font-weight: 400; fill: var(--navy); font-size: 13px; }
  .lid-title { fill: var(--gold); font-size: 21px; }
  .lid-copy { font-family: 'Oswald', sans-serif; font-weight: 400; fill: var(--paper); font-size: 11px; }
  .website { font-family: 'Tinos', serif; fill: var(--navy); font-size: 18px; }
  .dash { stroke: var(--gold); stroke-width: 5; }
</style>
</head>
<body>
<svg class="dieline" viewBox="122 820 1688 1070" preserveAspectRatio="xMidYMid meet" xmlns="http://www.w3.org/2000/svg">
  <!-- lid -->
  <path class="navy" d="M544,1288 V845 Q544,820 569,820 H941 Q966,820 966,845 V1288 Z"/>
  <!-- dust flaps -->
  <path class="paper" d="M122,1290 V1255 L172,1092 Q178,1075 196,1075 H510 Q533,1075 533,1098 V1290 Z"/>
  <path class="paper" d="M978,1290 V1098 Q978,1075 1001,1075 H1312 Q1330,1075 1336,1092 L1388,1255 V1290 Z"/>
  <path class="paper" d="M1537,1290 V1254 Q1537,1240 1551,1240 H1646 Q1660,1240 1660,1254 V1290 Z"/>
  <!-- body panels -->
  <rect class="paper" x="122" y="1288" width="1688" height="330"/>
  <!-- bottom flaps -->
  <path class="paper" d="M122,1615 V1815 Q122,1830 137,1830 H318 Q333,1830 333,1815 V1720 L544,1615 Z"/>
  <path class="paper" d="M544,1610 V1890 H648 V1830 H862 V1890 H966 V1610 Z"/>
  <path class="paper" d="M966,1615 L1178,1720 V1815 Q1178,1830 1193,1830 H1373 Q1388,1830 1388,1815 V1615 Z"/>
  <path class="paper" d="M1388,1615 L1495,1890 H1703 L1810,1615 Z"/>

  <!-- side bands -->
  <rect class="pattern" x="122" y="1296" width="422" height="189" role="img" aria-label="Navy band with fine geometric line pattern"/>
  <rect class="pattern" x="966" y="1296" width="422" height="189" role="img" aria-label="Navy band with fine geometric line pattern"/>
  <!-- front and back waves -->
  <path class="navy" d="M544,1296 H966 V1485 C930,1495 900,1515 860,1528 C780,1552 660,1545 544,1488 Z"/>
  <path class="navy" d="M1388,1296 H1810 V1485 C1774,1495 1744,1515 1704,1528 C1624,1552 1504,1545 1388,1488 Z"/>
  <rect class="gold-band" x="122" y="1288" width="1688" height="8"/>

  <!-- lid artwork (printed upside down) -->
  <g transform="rotate(180 755 1054)">
    <text class="heading lid-title" x="755" y="866" text-anchor="middle">LUMERRA RARE ESSENTIAL OILS DIFFUSER</text>
    <circle class="gold-dot" cx="755" cy="948" r="40"/>
    <text class="heading brand" x="755" y="1012" text-anchor="middle">LUMERRA</text>
    <text class="lid-copy" x="574" y="1058">Experience the pure essence of nature with the Rare Oils Aeri Diffuser. Sourced from the farthest</text>
    <text class="lid-copy" x="574" y="1072">reaches of the earth, Lumerra Rare Oils are extracted only from the highest quality and purest raw</text>
    <text class="lid-copy" x="574" y="1086">form ingredients. Using the Aeri diffuser with Lumerra Rare Oils can help improve health, quality of</text>
    <text class="lid-copy" x="574" y="1100">life, and overall spiritual balance.</text>
  </g>

  <!-- side panel: features -->
  <g class="side-panel features">
    <circle class="gold-dot" cx="333" cy="1375" r="40"/>
    <text class="heading brand" x="333" y="1442" text-anchor="middle">LUMERRA</text>
    <path class="navy" d="M122,1508 H240 A18.5,18.5 0 0 1 240,1545 H122 Z"/>
    <text class="heading pill-label" x="155" y="1535">FEATURES</text>
    <text class="bullet" x="155" y="1567">• Continuous diffusing</text>
    <text class="bullet" x="155" y="1583">• Timer settings</text>
    <text class="bullet" x="155" y="1599">• 7 LED color &amp; light settings</text>
    <text class="bullet" x="320" y="1567">• Portable</text>
    <text class="bullet" x="320" y="1583">• Pet safe</text>
    <text class="bullet" x="320" y="1599">• Easy to clean</text>
  </g>

  <!-- front panel -->
  <g class="front-panel">
    <text class="heading tagline" x="755" y="1323" text-anchor="middle">EXPERIENCE THE ESSENCE OF NATURE</text>
    <circle class="gold-dot" cx="755" cy="1375" r="40"/>
    <text class="heading brand" x="755" y="1442" text-anchor="middle">LUMERRA</text>
    <line class="dash" x1="674" y1="1485" x2="708" y2="1485"/>
    <line class="dash" x1="802" y1="1485" x2="836" y2="1485"/>
    <text class="heading product" x="755" y="1507" text-anchor="middle">AERI</text>
    <text class="heading collection" x="755" y="1575" text-anchor="middle">SIGNATURE RARE OILS COLLECTION</text>
    <text class="heading subtitle" x="755" y="1603" text-anchor="middle">ULTRASONIC DIFFUSER</text>
    <circle class="navy" cx="755" cy="1735" r="20"/>
    <text class="heading brand-navy" x="755" y="1775" text-anchor="middle">LUMERRA</text>
    <text class="website" x="755" y="1797" text-anchor="middle">www.lumerra.com</text>
  </g>

  <!-- side panel: specifications -->
  <g class="side-panel specifications">
    <circle class="gold-dot" cx="1177" cy="1375" r="40"/>
    <text class="heading brand" x="1177" y="1442" text-anchor="middle">LUMERRA</text>
    <path class="navy" d="M966,1508 H1126 A18.5,18.5 0 0 1 1126,1545 H966 Z"/>
    <text class="heading pill-label" x="998" y="1535">SPECIFICATIONS</text>
    <text class="bullet" x="998" y="1567">• Dimensions: 135*135*108mm</text>
    <text class="bullet" x="998" y="1583">• Capacity: 300ml</text>
    <text class="bullet" x="998" y="1599">• 33 ml/hour output</text>
    <text class="bullet" x="1163" y="1567">• Safety Auto-off when empty</text>
    <text class="bullet" x="1163" y="1583">• Whisper Quiet</text>
    <text class="bullet" x="1163" y="1599">• Contains 1 Aeri Diffuser, 1 Power Adaptor</text>
  </g>

  <!-- back panel -->
  <g class="back-panel">
    <text class="heading tagline" x="1599" y="1323" text-anchor="middle">EXPERIENCE THE ESSENCE OF NATURE</text>
    <circle class="gold-dot" cx="1599" cy="1375" r="40"/>
    <text class="heading brand" x="1599" y="1442" text-anchor="middle">LUMERRA</text>
    <line class="dash" x1="1518" y1="1485" x2="1552" y2="1485"/>
    <line class="dash" x1="1646" y1="1485" x2="1680" y2="1485"/>
    <text class="heading product" x="1599" y="1507" text-anchor="middle">AERI</text>
    <text class="heading collection" x="1599" y="1575" text-anchor="middle">SIGNATURE RARE OILS COLLECTION</text>
    <text class="heading subtitle" x="1599" y="1603" text-anchor="middle">ULTRASONIC DIFFUSER</text>
  </g>
</svg>
</body>
</html>
```